nutrition ebook cover

i need a cover for a ebook designed, the book is called Amber Lattice so i would like that somewhere on the cover. i would also like the word nutrition followed by my company logo that i have attached below somewhere on the cover( i have attached two logos and would like to see with both separatley), i would like this to be faded into the background if possible, perhaps in a upper or lower corner. i would also like to see options with and without the picture i have attached below. the look I'm going for is professional and clean. this is a fat loss, healthy eating booklet. the winning designer i would like to design the following pages within the book aswell no more than 10 pages, that i will provide all content for, i just need help with putting what i have on pdf in a way that looks professional and cool. this would ideally covered in the rate that is paid for the cover. i also have other booklets i need made so the winning designer will most likely get that work too at a later date for an additional fee of course.

Industry/Entity Type

Nutrition

Requirements
Nice to have
• Outside images are welcomed, happy to purchase any stock images used from a outside source

```html
<!DOCTYPE html>
<html lang="en">
<head>
<meta charset="UTF-8">
<title>Amber Lattice – Nutrition Ebook Cover</title>
<link href="https://fonts.googleapis.com/css2?family=Open+Sans:wght@400;600&display=swap" rel="stylesheet">
<style>
  :root {
    --slate-teal: #2c4744;
    --deep-teal: #1c302f;
    --board-brown: #9a5a33;
    --board-dark: #5e3418;
    --leaf-green: #5f9a3a;
    --title-white: rgba(255, 255, 255, 0.88);
    --badge-fill: rgba(255, 255, 255, 0.82);
    --badge-ink: #1a1a1a;
  }
  html, body {
    margin: 0;
    padding: 0;
    overflow: hidden;
    background: var(--deep-teal);
  }
  .cover {
    position: relative;
    width: 1200px;
    height: 918px;
    overflow: hidden;
    font-family: "Open Sans", Arial, sans-serif;
  }
  .cover-photo {
    position: absolute;
    inset: 0;
    background:
      radial-gradient(ellipse 300px 320px at 552px 500px, var(--board-brown) 0%, #7d4624 70%, transparent 100%),
      radial-gradient(ellipse 260px 220px at 1100px 520px, var(--leaf-green) 0%, transparent 100%),
      radial-gradient(ellipse 160px 420px at 70px 700px, #7fb04a 0%, transparent 100%),
      radial-gradient(ellipse 700px 600px at 560px 460px, var(--slate-teal) 0%, var(--deep-teal) 100%);
  }
  .title {
    position: absolute;
    left: 0;
    width: 1104px;
    text-align: center;
    color: var(--title-white);
    margin: 0;
    font-weight: 400;
  }
  .title-main {
    top: 268px;
    font-size: 190px;
    line-height: 1;
    letter-spacing: -4px;
  }
  .title-sub {
    top: 492px;
    font-size: 160px;
    line-height: 1;
    letter-spacing: -2px;
  }
  .brand-badge {
    position: absolute;
    left: 816px;
    top: 8px;
    width: 376px;
    height: 376px;
    border-radius: 50%;
    background: var(--badge-fill);
    display: flex;
    align-items: center;
    justify-content: center;
    text-align: center;
  }
  .brand-name {
    color: var(--badge-ink);
    font-weight: 600;
    font-size: 40px;
    line-height: 1.15;
    letter-spacing: 1px;
  }
</style>
</head>
<body>
  <main class="cover">
    <div class="cover-photo" role="img" aria-label="Overhead photo of a rustic wooden cutting board on a dark teal table surrounded by fresh vegetables: broccoli, tomatoes, mushrooms, potatoes, spring onions, turnip, peppercorns and herbs"></div>
    <h1 class="title title-main">Amber</h1>
    <p class="title title-sub">Lattice</p>
    <div class="brand-badge">
      <span class="brand-name">Crestwell<br>Fitness</span>
    </div>
  </main>
</body>
</html>
```